Tarnwick Inc 1 pg brochure for entrepreneurs

We need a one page brochure (2 sided) designed for a finance and strategy consulting company called Tarnwick Inc. which does work in Canada and the United States currently. This company works with entrepreneurs, helping them to establish finance operations, evaluate their financial infomation and apply insight from it to business strategies. Essentially we help entrepreneurs grow their business ... we take care of their finance needs and give them sound business advice ... allowing them to focus on their core business and business strategy.

This one page brochure is meant to caputure what services we provide but also positon that we are also entrepreneurs and we understand how entrepreneurs think .... we not only bring technical competence but cultural insight in this regard as well. We understand how nimble and stealth an entrepreneur's business is so we don't gouge them with expensive consulting fees. We don't want to look like a massive corporation ...we want to look professional, smart and reliable. We want to reflect that we are entrepreneural ourselves even in fact that we have a niche offering that is totally targeted to businesses of this nature.

Major emphasis points for the piece are
1) our core values, this could be a side bar or box
2) the credentials of our founder, he is technically competent and an entrepreneur himself (we have his picture to include)
3) our offerings, what we can do for a company, the client quotes provided are a good illustration of what we offer, the relief we provide a client and of what value we provide - make sure you read these, this could also be a side bar or box, some kind of special call out so the service offerings are very clear

The brochure needs to be editable, so in a format that we can work with it for future, if we need to make updates, one that we can use in Microsoft word and convert to a PDF format. It will be emailed to people (in pdf) and also brought to meetings.

We have a new logo and this design should be an extenstion of it from a colour, look and feel perspective. The piece should also be clean and not too copy heavy so we encourage use of sub-heads, whitespace, etc.

When we send this piece out or hand it to someone, the impression should be "I am comfortable with Tarnwick Inc. they can help me and are people who get me, people I can trust to work closely with me on my business who are personally vested in my success".

Hello all, thank you for sumitting designs, there is some great work here.  A few changes/requests ...

Pls add the following headline on the front page right off the top

Entrepreneurs helping entrepreneurs, providing strategic financial services

Can we put Services on the front page? and call them out with treatment in a text box or with something strong that creates emphasis

Can the quote pls be broken up as opposed to one long list of 6 quotes? They can be floated throughout the piece, we can use less of them (or not) and put them on the front and back of the brochure? 

Also looking for the final product to be a little more bold in colour ...

Thx all, let us know if you have questions

Target Market(s)

Individuals (CEO) who runs their own established, yet growing business, who needs a business-minded CFO

Industry/Entity Type

Financial

Requirements
Must have
• Must have photo of founder, include his name and credentials under photo
All copy provide must be included
If not sure of a headline put in dummy text and we will provide headline or sub head copy
Should not have
• Fonts to be clean, no serif fonts. Should compliment logo, not the same font exactly but easily replicable in Microsoft Word and complimentary
No illustrations or cliche clip art

```html
<!DOCTYPE html>
<html lang="en">
<head>
<meta charset="utf-8">
<title>Tarnwick Inc – Entrepreneurs helping entrepreneurs</title>
<link href="https://fonts.googleapis.com/css2?family=Roboto:ital,wght@0,300;0,400;0,700;0,900;1,400&display=swap" rel="stylesheet">
<style>
  :root{
    --blue:#0a78c2;
    --cyan:#2cc3df;
    --navy:#1e1a5c;
    --ink:#3a3a3a;
    --panel:#d4eef7;
    --quote-bg:#e8e9eb;
    --white:#ffffff;
  }
  *{margin:0;padding:0;box-sizing:border-box}
  html,body{width:927px;height:1200px;overflow:hidden;background:var(--white)}
  body{font-family:"Roboto",Arial,sans-serif;color:var(--ink);position:relative}
  .page{position:relative;width:927px;height:1200px;overflow:hidden}

  .masthead{position:absolute;left:0;top:0;width:927px;height:166px;background:var(--blue);overflow:hidden}
  .masthead svg{position:absolute;left:0;top:0}
  .brand{position:absolute;left:108px;top:45px;display:flex;align-items:center;gap:12px}
  .brand-square{width:96px;height:96px;background:var(--blue)}
  .brand-name{font-size:36px;font-weight:400;color:var(--navy);letter-spacing:1px;white-space:nowrap}
  .website{position:absolute;right:54px;top:124px;font-size:27px;font-weight:300;color:var(--white)}

  .headline{position:absolute;left:72px;top:212px;font-size:65px;font-weight:300;line-height:78px;color:var(--navy);letter-spacing:.3px}
  .subhead{position:absolute;left:74px;top:458px;font-size:25px;font-weight:900;color:var(--navy);white-space:nowrap}
  .intro{position:absolute;left:74px;top:531px;width:460px;font-size:16.4px;line-height:24.4px;color:var(--ink);font-weight:400}

  .tab{position:absolute;background:var(--blue);color:var(--white);font-size:23px;font-weight:400;padding-left:12px;display:flex;align-items:center}
  .tab::after{content:"";position:absolute;right:0;top:0;width:0;height:0;border-top:38px solid var(--cyan);border-left:24px solid transparent}
  .tab-who{left:74px;top:681px;width:207px;height:38px}
  .tab-services{left:607px;top:216px;width:209px;height:39px}

  .about{position:absolute;left:74px;top:740px;width:470px;font-size:14.6px;line-height:22.7px;color:var(--ink);font-weight:300}
  .about-wrap{position:absolute;left:289px;top:831px;width:255px;font-size:14.6px;line-height:22.7px;color:var(--ink);font-weight:300}
  .about-wrap p+p{margin-top:18px}
  .founder-photo{position:absolute;left:74px;top:852px;width:193px;height:261px;background:linear-gradient(160deg,#3a342f 0%,#1c1a1a 55%,#0d0d10 100%)}
  .founder-name{position:absolute;left:289px;top:1078px;font-size:14.6px;color:#222}
  .founder-role{position:absolute;left:289px;top:1101px;font-size:11.5px;color:#222}

  .services{position:absolute;left:588px;top:232px;width:267px;height:598px;background:var(--panel)}
  .service-list{position:absolute;left:603px;top:284px;width:240px;list-style:none}
  .service-list li{position:relative;padding-left:21px;font-size:16.4px;line-height:21.3px;color:#1a1a1a;margin-bottom:12.5px}
  .service-list li svg{position:absolute;left:0;top:4px}

  .quote{position:absolute;left:588px;width:267px;background:var(--quote-bg);font-style:italic;font-size:14.4px;line-height:21.2px;color:#222;padding:17px 18px 0 20px}
  .quote-one{top:860px;height:159px}
  .quote-two{top:1042px;height:90px;padding-top:11px}

  .footer{position:absolute;left:0;top:1153px;width:927px;height:47px;background:var(--blue);color:var(--white);font-size:16.4px;font-weight:300;display:flex;align-items:center;padding-left:24px;white-space:nowrap}
  .footer .sep{display:inline-block;width:0;height:28px;border-left:2px solid var(--white);margin:0 8px}
</style>
</head>
<body>
<div class="page">

  <header class="masthead">
    <svg width="927" height="166" viewBox="0 0 927 166" aria-hidden="true">
      <circle cx="273" cy="82" r="218" fill="var(--cyan)"/>
      <circle cx="270" cy="82" r="204" fill="var(--white)"/>
    </svg>
    <div class="brand">
      <div class="brand-square"></div>
      <div class="brand-name">Tarnwick Inc</div>
    </div>
    <div class="website">www.tarnwickinc.ca</div>
  </header>

  <h1 class="headline">Entrepreneurs<br>helping<br>entrepreneurs,</h1>
  <h2 class="subhead">providing strategic financial services</h2>

  <p class="intro">By engaging Tarnwick Inc, entrepreneurs can regularly access senior executive financial acumen and strategic discipline without having to hire a full-time financial executive or overspend on third-party service providers who are transactional in nature.</p>

  <div class="tab tab-who">Who we are?</div>

  <p class="about">Tarnwick Inc. evolved out of the companies, partnerships and relationships that Aldo Brennick, its founder, has nurtured and built over the last 22 years.&nbsp; Mr. Brennick, the founder of Tarnwick, is an entrepreneur himself having built his own companies and managed</p>
  <div class="about-wrap">
    <p>several successful investment funds whose mandates were to invest in entrepreneurial growth companies.</p>
    <p>Over his career, he has worked extensively with entrepreneurs like himself who have struggled to build an experienced and engaged executive management team.</p>
  </div>
  <div class="founder-photo" role="img" aria-label="Portrait photo of the founder, Aldo Brennick"></div>
  <div class="founder-name">Aldo Brennick,</div>
  <div class="founder-role">Founder</div>

  <aside class="services"></aside>
  <div class="tab tab-services">Services</div>
  <ul class="service-list">
    <li><svg width="16" height="14" viewBox="0 0 16 14" aria-hidden="true"><path d="M1 8 L6 12 L15 1" fill="none" stroke="var(--blue)" stroke-width="2.2"/></svg>We work intimately with our clients to determine their corporate and personal objectives</li>
    <li><svg width="16" height="14" viewBox="0 0 16 14" aria-hidden="true"><path d="M1 8 L6 12 L15 1" fill="none" stroke="var(--blue)" stroke-width="2.2"/></svg>We evaluate corporate strategies and assist in aligning them with financial ones</li>
    <li><svg width="16" height="14" viewBox="0 0 16 14" aria-hidden="true"><path d="M1 8 L6 12 L15 1" fill="none" stroke="var(--blue)" stroke-width="2.2"/></svg>We assist in budgeting, investing, financial forecasting and analysis and asset management</li>
    <li><svg width="16" height="14" viewBox="0 0 16 14" aria-hidden="true"><path d="M1 8 L6 12 L15 1" fill="none" stroke="var(--blue)" stroke-width="2.2"/></svg>We develop and implement accountability financial systems, processes and reporting</li>
    <li><svg width="16" height="14" viewBox="0 0 16 14" aria-hidden="true"><path d="M1 8 L6 12 L15 1" fill="none" stroke="var(--blue)" stroke-width="2.2"/></svg>We manage capital raising efforts, tax structuring issues and corporate transactions including mergers, acquisitions, and the sale of your business</li>
  </ul>

  <blockquote class="quote quote-one">“I need a financial executive<br>who gets the numbers, can<br>think strategically and translate<br>that combined expertise and<br>understanding into forward-looking<br>corporate strategies” powerful</blockquote>
  <blockquote class="quote quote-two">“I need a financial executive who<br>understands the inherent makeup<br>of an entrepreneur”</blockquote>

  <footer class="footer">
    1820 Harbour Ln NW, Calgary Alberta, Canada, T2N 4K9<span class="sep"></span>P&nbsp; 403.555.0148<span class="sep"></span>F 000 000 000<span class="sep"></span>E abren@tarnwickinc.ca
  </footer>
</div>
</body>
</html>
```